New Joomla Website for Marquee Hire Co

We need a web design for our new Marquee Hire Co here in New Zealand called Breezy Canopies.
We rather like the retro look, as it fit very well with the current trends in weddings that is a more of a retro look (and we had our logo designed to reflect that!). The 50's and 60's wedding styles are really making a comeback. We would like to communicate to that market effectively.

The Home page should have a slider image with space for a headline on it. It is a visual product we have (but we are selling that dream of a perfect wedding/party/event).

Our competition here have a really nice site that you could look at - www.plovanta.co.nz

The other pages would have space for a picture, and then a blurb under each element related to it.
We will have a FAQ, Gallery, Hire and Contact us pages - we will add them as we go along.

From a technical perspective, we are using Joomla 2.5 and upwards.

Any questions - let me know. I look forward seeing the designs!

Target Market(s)

Couples looking for a wedding marquee, birthday parties, Corporate events

Industry/Entity Type

Wedding

Requirements
Must have
• 1. Preferably done in Joomla. I will also look at Wordpress site.
2. It has to have a retro look and feel.
3. It has to use my brand new logo (included)

```html
<!DOCTYPE html>
<html lang="en">
<head>
<meta charset="utf-8">
<title>Breezy Canopies – Marquee Hire New Zealand</title>
<link href="https://fonts.googleapis.com/css2?family=Cabin:wght@400;500;600;700&family=Encode+Sans+Condensed:wght@300;400&display=swap" rel="stylesheet">
<style>
:root{
  --ink:#3d3427;
  --brown:#7a5a32;
  --brown-dark:#5f4424;
  --blue:#5e87aa;
  --blue-dark:#4a7192;
  --blue-light:#86a9c6;
  --heading-blue:#4f7ca3;
  --cream:#fcf8e5;
  --cream-edge:#efe4bd;
  --parchment:#e7d49a;
  --footer-top:#a8844f;
  --footer-bottom:#8e6b3d;
  --bar-blue:#a7c3dc;
  --white:#ffffff;
}
*{box-sizing:border-box;margin:0;padding:0}
html,body{width:990px;height:1200px;overflow:hidden}
body{
  position:relative;
  font-family:"Cabin",sans-serif;
  color:var(--ink);
  background:
    radial-gradient(ellipse at 20% 40%, rgba(255,245,205,.55), transparent 60%),
    radial-gradient(ellipse at 85% 70%, rgba(200,165,95,.35), transparent 55%),
    radial-gradient(ellipse at 10% 90%, rgba(190,150,80,.3), transparent 50%),
    var(--parchment);
}
.abs{position:absolute}
.header{position:absolute;left:0;top:0;width:990px;height:160px;background:var(--white);border-top:3px solid #7d6845}

.brand{left:99px;top:44px;display:flex;align-items:center;gap:10px}
.brand-dot{width:40px;height:40px;border-radius:50%;background:var(--blue-light)}
.brand-name{font-size:24px;font-weight:700;color:var(--brown)}

.call-tab{left:755px;top:0;width:134px;height:31px;background:linear-gradient(var(--blue-light),var(--blue));border-radius:0 0 8px 8px;box-shadow:0 2px 3px rgba(0,0,0,.25);display:flex;align-items:center;justify-content:center;gap:8px;color:var(--white);font-size:13px;font-weight:500}

.follow{left:689px;top:61px;font-size:12px;font-weight:500;color:var(--brown-dark)}
.socials{left:756px;top:53px;display:flex;gap:6px}
.socials span{width:22px;height:22px;border-radius:3px;display:block}

.search{left:693px;top:92px;width:198px;height:25px;border:1px solid #dcdcdc;border-radius:5px;background:linear-gradient(#f1f1f1,#fff)}
.search svg{position:absolute;right:6px;top:3px}

.nav{left:74px;top:132px;width:842px;height:43px}
.nav-band{position:absolute;left:14px;top:0;width:814px;height:43px;background:linear-gradient(var(--blue-light),var(--blue));border-top:1px dashed #d9e6f1;border-bottom:1px dashed #d9e6f1;outline:2px solid var(--blue-dark);outline-offset:-4px}
.nav a{position:absolute;top:13px;transform:translateX(-50%);color:var(--white);font-size:13px;font-weight:600;text-decoration:none}
.nav .sep{position:absolute;top:6px;width:1px;height:31px;background:rgba(255,255,255,.3)}

.slider{left:97px;top:169px;width:796px;height:322px;border:2px solid var(--white);box-shadow:0 1px 4px rgba(0,0,0,.3);background:linear-gradient(180deg,#5d7a3a 0%,#8fae6a 25%,#e9ecef 45%,#d7d5d2 60%,#7a5a44 85%,#6f8a88 100%)}
.slide-panel{left:629px;top:190px;width:227px;height:287px;background:rgba(25,22,18,.82);padding:16px 29px 0 28px;color:var(--white)}
.slide-title{font-family:"Encode Sans Condensed",sans-serif;font-weight:300;font-size:44px;line-height:50px;letter-spacing:1px}
.slide-text{margin-top:16px;font-size:11px;line-height:20px;color:#eee}
.btn-cream{display:flex;align-items:center;gap:6px;background:linear-gradient(#fbf6d9,#e8dcae);color:var(--brown-dark);font-size:11px;font-weight:600;border-radius:3px;box-shadow:0 1px 3px rgba(0,0,0,.3)}
.slide-btn{position:absolute;left:31px;top:205px;height:37px;padding:0 12px}
.arrow-btn{width:28px;height:28px;border-radius:50%;background:#3b3834;border:2px solid #e8e4da;display:flex;align-items:center;justify-content:center}

.panel{background:var(--cream);border:1px solid var(--cream-edge);border-radius:4px;box-shadow:0 1px 3px rgba(120,90,40,.2)}
.btn-blue{position:absolute;height:31px;background:linear-gradient(var(--blue-light),var(--blue));color:var(--white);font-size:11px;font-weight:600;border-radius:3px;display:flex;align-items:center;justify-content:center;box-shadow:0 1px 2px rgba(0,0,0,.3)}

.welcome{left:97px;top:520px;width:555px;height:208px}
.welcome-photo{left:18px;top:21px;width:181px;height:126px;border:2px solid #5b4a36;background:linear-gradient(135deg,#f3f1ee 0%,#d9d6d1 45%,#3a3a3a 60%,#8d8a86 100%)}
.welcome h1{position:absolute;left:221px;top:20px;font-size:16px;font-weight:600;color:var(--ink)}
.welcome h1 span{color:var(--heading-blue)}
.welcome p{position:absolute;left:221px;top:50px;width:320px;font-size:10px;line-height:20.4px}

.services{left:678px;top:518px;width:214px;height:206px}
.services h2{position:absolute;left:32px;top:20px;font-size:16px;font-weight:500;color:var(--brown-dark)}
.services ul{position:absolute;left:22px;top:44px;list-style:none}
.services li{display:flex;align-items:center;gap:14px;height:20.6px;font-size:10px}

.gallery{left:98px;top:745px;width:795px;height:210px}
.gallery h2{position:absolute;left:28px;top:8px;font-size:16px;font-weight:500;color:var(--brown-dark)}
.gallery .pager{position:absolute;right:14px;top:8px;display:flex;gap:8px}
.shot{position:absolute;top:33px;height:157px;border:1px solid #bda77a}

.footer{left:97px;top:969px;width:796px;height:183px;background:linear-gradient(var(--footer-top),var(--footer-bottom))}
.quote h3{position:absolute;left:34px;top:50px;font-size:14px;font-weight:600;color:var(--white)}
.quote p{position:absolute;left:34px;top:75px;width:215px;font-size:9.5px;line-height:15px;color:var(--white);font-weight:500}
.quote-btn{position:absolute;left:33px;top:133px;height:31px;padding:0 10px}

.newsletter{left:291px;top:13px;width:206px;height:149px;background:#f7f2ea;transform:rotate(2deg);box-shadow:0 2px 5px rgba(0,0,0,.35)}
.newsletter-back{left:286px;top:22px;width:200px;height:140px;background:#e6ddd0;transform:rotate(-3deg)}
.newsletter p{position:absolute;left:27px;top:24px;width:170px;font-size:10.5px;line-height:15px;color:var(--ink)}
.nl-input{position:absolute;left:15px;top:78px;width:176px;height:25px;border:1px solid #d8d0c2;border-radius:13px;background:var(--white);font-size:10px;color:#999;padding:5px 14px}
.nl-icon{position:absolute;left:165px;top:74px;width:30px;height:30px;border-radius:50%;background:#e05a78;border:2px solid #fff;display:flex;align-items:center;justify-content:center}
.nl-btn{position:absolute;left:25px;top:106px;width:74px;height:27px;background:var(--brown);border-radius:3px;color:var(--white);font-size:11px;font-weight:600;display:flex;align-items:center;justify-content:center}

.contact h3{position:absolute;left:547px;top:44px;font-size:14px;font-weight:500;color:var(--white)}
.contact .row{position:absolute;left:547px;display:flex;align-items:flex-start;gap:10px;color:var(--white);font-weight:600}

.bottom-bar{left:97px;top:1152px;width:796px;height:48px;background:linear-gradient(var(--bar-blue),#c5d8e8)}
.bottom-bar .copy{position:absolute;left:20px;top:17px;font-size:10px;color:var(--ink)}
.bottom-bar a{position:absolute;top:17px;font-size:10px;color:var(--ink);text-decoration:none}
</style>
</head>
<body>

<header class="header">
  <div class="abs brand"><span class="brand-dot"></span><span class="brand-name">Breezy Canopies</span></div>

  <div class="abs call-tab">
    <svg width="12" height="14" viewBox="0 0 12 14"><path d="M3 1 L5 4 L3.5 5.5 Q5 9 7.5 10.5 L9 9 L11.5 11 L10 13 Q3 12 1 3 Z" fill="#fff"/></svg>
    Call us now
  </div>

  <div class="abs follow">Follow Us</div>
  <div class="abs socials" role="img" aria-label="Social network links">
    <span style="background:#4a67a8"></span>
    <span style="background:#5dbde8"></span>
    <span style="background:#c8202a"></span>
    <span style="background:#333"></span>
    <span style="background:#c4302b"></span>
  </div>

  <div class="abs search">
    <svg width="22" height="18" viewBox="0 0 22 18"><circle cx="8" cy="7" r="5.5" fill="none" stroke="#4f7ca3" stroke-width="2.2"/><line x1="12" y1="11" x2="19" y2="16" stroke="#4f7ca3" stroke-width="3" stroke-linecap="round"/></svg>
  </div>
</header>

<nav class="abs nav">
  <svg class="abs" style="left:0;top:2px" width="842" height="43" viewBox="0 0 842 43">
    <polygon points="0,3 20,3 20,43 10,43 16,23" fill="#4a7192"/>
    <polygon points="842,3 822,3 822,43 832,43 826,23" fill="#4a7192"/>
  </svg>
  <div class="nav-band"></div>
  <span class="sep" style="left:166px"></span>
  <span class="sep" style="left:323px"></span>
  <span class="sep" style="left:486px"></span>
  <span class="sep" style="left:650px"></span>
  <a style="left:85px">Home</a>
  <a style="left:235px">FAQ</a>
  <a style="left:403px">Gallery</a>
  <a style="left:569px">Hire</a>
  <a style="left:739px">Contact Us</a>
</nav>

<section class="abs slider" role="img" aria-label="Guests mingling outside a large white stretch marquee in a leafy garden"></section>
<div class="abs slide-panel">
  <div class="slide-title">Breezy<br>Canopies</div>
  <p class="slide-text">Lorem ipsum dolor sit amet con-sectetueradpi scinesent ves tibm moeaeanuu uuiol.</p>
  <div class="btn-cream slide-btn">Read More
    <svg width="12" height="12" viewBox="0 0 12 12"><circle cx="6" cy="6" r="5" fill="#fff" stroke="#cbbf9a"/><path d="M5 3.5 L7.5 6 L5 8.5" fill="none" stroke="#9a8a60"/></svg>
  </div>
</div>
<div class="abs arrow-btn" style="left:84px;top:316px">
  <svg width="14" height="12" viewBox="0 0 14 12"><path d="M13 6 H3 M7 1 L2 6 L7 11" fill="none" stroke="#fff" stroke-width="2.4"/></svg>
</div>
<div class="abs arrow-btn" style="left:879px;top:315px">
  <svg width="14" height="12" viewBox="0 0 14 12"><path d="M1 6 H11 M7 1 L12 6 L7 11" fill="none" stroke="#fff" stroke-width="2.4"/></svg>
</div>

<section class="abs panel welcome">
  <div class="abs welcome-photo" role="img" aria-label="Event coordinator standing in front of a presentation screen"></div>
  <h1>Welcome to the <span>Breezy Canopies</span></h1>
  <p>Lorem ipsum dolor sit amet consectetueradpi scinesent ves tibml moeaeanuu uuiol. Lorem ipsum dolor sit amet consectetueradpik scinesent ves tibm moeaeanuu uuioltibm moeap&nbsp; anuu uuioluuiol ibm moea Lorem ipsum dolor sit ametaso tconsecase ertold dolor sit ametaso tconsecase ertolds.</p>
  <div class="btn-blue" style="left:222px;top:162px;width:87px">Read More</div>
</section>

<section class="abs panel services">
  <h2>Services</h2>
  <ul>
    <li><svg width="6" height="9" viewBox="0 0 6 9"><path d="M1 1 L5 4.5 L1 8" fill="none" stroke="#4f7ca3" stroke-width="1.8"/></svg>Event planning and co-ordination</li>
    <li><svg width="6" height="9" viewBox="0 0 6 9"><path d="M1 1 L5 4.5 L1 8" fill="none" stroke="#4f7ca3" stroke-width="1.8"/></svg>Exceptional styling</li>
    <li><svg width="6" height="9" viewBox="0 0 6 9"><path d="M1 1 L5 4.5 L1 8" fill="none" stroke="#4f7ca3" stroke-width="1.8"/></svg>Creative theming</li>
    <li><svg width="6" height="9" viewBox="0 0 6 9"><path d="M1 1 L5 4.5 L1 8" fill="none" stroke="#4f7ca3" stroke-width="1.8"/></svg>Exclusive and private locations</li>
    <li><svg width="6" height="9" viewBox="0 0 6 9"><path d="M1 1 L5 4.5 L1 8" fill="none" stroke="#4f7ca3" stroke-width="1.8"/></svg>Innovative event catering</li>
  </ul>
  <div class="btn-blue" style="left:19px;top:160px;width:86px">Read More</div>
</section>

<section class="abs panel gallery">
  <h2>Our Gallery</h2>
  <div class="pager">
    <svg width="10" height="14" viewBox="0 0 10 14"><path d="M8 1 L2 7 L8 13" fill="none" stroke="#5f4424" stroke-width="2.6"/></svg>
    <svg width="10" height="14" viewBox="0 0 10 14"><path d="M2 1 L8 7 L2 13" fill="none" stroke="#9c8a6a" stroke-width="2.6"/></svg>
  </div>
  <div class="shot" style="left:12px;width:238px;background:linear-gradient(180deg,#6f8f4a 0%,#d8a060 30%,#e8ecee 55%,#cfd6d8 100%)" role="img" aria-label="Banquet tables with white linen and floral centrepieces"></div>
  <div class="shot" style="left:271px;width:250px;background:radial-gradient(ellipse at 55% 35%,#7aa6d6 0%,#8a2a20 40%,#2a1510 80%)" role="img" aria-label="Evening party under marquee with stage lights"></div>
  <div class="shot" style="left:539px;width:243px;background:linear-gradient(90deg,#1c1c1e 0%,#3a3a3c 40%,#e9e9e6 50%,#2a2a2c 70%,#1a1a1a 100%)" role="img" aria-label="Bar display with white roses, champagne bottles and glassware"></div>
</section>

<footer class="abs footer">
  <div class="quote">
    <h3>GET A QUOTE</h3>
    <p>By choosing Plovanta, you'll be looking for something that stands out from the 'normal' event.</p>
    <div class="btn-cream quote-btn">Get a Quote
      <svg width="14" height="10" viewBox="0 0 14 10"><path d="M1 1 L5 5 L1 9 M7 1 L11 5 L7 9" fill="none" stroke="#4f7ca3" stroke-width="1.5"/></svg>
    </div>
  </div>

  <div class="abs newsletter-back"></div>
  <div class="abs newsletter">
    <p>Sign up for our newletter for ideas !</p>
    <div class="nl-input">Enter your email..</div>
    <div class="nl-icon"><svg width="16" height="11" viewBox="0 0 16 11"><rect x="1" y="1" width="14" height="9" fill="none" stroke="#fff" stroke-width="1.4"/><path d="M1 1 L8 6 L15 1" fill="none" stroke="#fff" stroke-width="1.4"/></svg></div>
    <div class="nl-btn">Sign Up</div>
  </div>

  <div class="contact">
    <h3>Contact Us</h3>
    <div class="row" style="top:72px;font-size:14px;font-weight:500">
      <svg width="14" height="15" viewBox="0 0 12 14"><path d="M3 1 L5 4 L3.5 5.5 Q5 9 7.5 10.5 L9 9 L11.5 11 L10 13 Q3 12 1 3 Z" fill="#fff"/></svg>+64 21 555 0142
    </div>
    <div class="row" style="top:99px;font-size:10.5px">
      <svg width="18" height="12" viewBox="0 0 18 12"><rect x="1" y="1" width="16" height="10" fill="none" stroke="#fff" stroke-width="1.3"/><path d="M1 1 L9 7 L17 1" fill="none" stroke="#fff" stroke-width="1.3"/></svg>hello@breezycanopies.co.nz
    </div>
    <div class="row" style="top:127px;font-size:10.5px;line-height:14px">
      <svg width="18" height="22" viewBox="0 0 18 22"><path d="M9 1 C4 1 1 4.5 1 8.5 C1 13 9 21 9 21 C9 21 17 13 17 8.5 C17 4.5 14 1 9 1 Z" fill="#d6302a"/><circle cx="9" cy="8" r="3" fill="#fff"/></svg>
      <span>18 Harlow Lane, Kerrin,<br>New Zealand</span>
    </div>
  </div>
</footer>

<div class="abs bottom-bar">
  <span class="copy">©2013 Breezy Canopies. All right Reserved</span>
  <a style="left:461px">Home</a>
  <a style="left:520px">FAQ</a>
  <a style="left:582px">Gallery</a>
  <a style="left:664px">Hire</a>
  <a style="left:719px">Contact Us</a>
</div>

</body>
</html>
```